Flyer-Design für Basilikum frisch-gruen-kochen-schlemmen
Zielgruppe
Hallo wir brauchen wieder Flyer für unser Lokal in Frankfurt. Es soll jetzt nichts besonderes beworben werden, also 'nur' Info wie das es uns gibt, wo wir zu finden sind, Kontaktdaten, Öffnungszeiten etc. Gedacht sind die Flyer quasi als Imageflyer.
Aufgabenstellung
Wir haben schonmal Flyer verwendet die ich selbst gestaltet habe, jetzt soll etwas neues, zeitgemässes her.
Göße: A6

```html
<!DOCTYPE html>
<html lang="de">
<head>
<meta charset="utf-8">
<title>Basilikum – Imageflyer</title>
<link rel="stylesheet" href="https://fonts.googleapis.com/css2?family=Barlow:wght@400;700&display=swap">
<style>
  :root {
    --bg: #d9d9d9;
    --green: #76b82a;
    --red: #7d1610;
    --white: #ffffff;
    --ink: #111111;
    --photo-warm-a: #c98a55;
    --photo-warm-b: #7a3a1c;
    --photo-fresh-a: #8fb07a;
    --photo-fresh-b: #e8ebe6;
    --photo-sweet-a: #e9d7a3;
    --photo-sweet-b: #5a2a22;
  }
  * { margin: 0; padding: 0; box-sizing: border-box; }
  html, body { width: 1200px; height: 900px; overflow: hidden; }
  body { background: var(--bg); font-family: "Barlow", Arial, sans-serif; }

  .flyer {
    position: absolute; left: 310px; top: 40px;
    width: 580px; height: 820px;
    background: var(--green);
    overflow: hidden;
    box-shadow: 0 6px 18px rgba(0,0,0,.25);
  }
  .photo { position: absolute; }
  .photo--main { left: 0; top: 0; width: 262px; height: 262px;
    background: radial-gradient(circle at 55% 40%, #d8452a 0 18%, var(--photo-warm-a) 45%, var(--photo-warm-b) 100%); }
  .photo--wrap { left: 0; top: 276px; width: 232px; height: 272px;
    background: radial-gradient(circle at 60% 50%, var(--photo-fresh-a) 0 35%, #b89c74 55%, var(--photo-fresh-b) 100%); }
  .photo--dessert { left: 0; top: 564px; width: 232px; height: 256px;
    background: linear-gradient(180deg, var(--photo-sweet-b) 0 10%, var(--photo-sweet-a) 45%, #c9a070 75%, #f2f0ec 100%); }

  .rule { position: absolute; background: var(--white); }
  .rule--top-v  { left: 268px; top: 0;     width: 3px; height: 168px; }
  .rule--band-t { left: 240px; top: 167px; width: 320px; height: 2px; }
  .rule--band-b { left: 240px; top: 263px; width: 320px; height: 2px; }
  .rule--col-v  { left: 240px; top: 265px; width: 3px; height: 555px; }
  .rule--row-1  { left: 0;     top: 267px; width: 240px; height: 3px; }
  .rule--row-2  { left: 0;     top: 555px; width: 240px; height: 3px; }

  .brand-band {
    position: absolute; left: 240px; top: 169px; width: 320px; height: 94px;
    background: var(--red); color: var(--white);
    display: flex; flex-direction: column; justify-content: center; align-items: center;
  }
  .brand-name { font-weight: 700; font-size: 38px; line-height: 1; letter-spacing: 1px; }
  .brand-claim { font-weight: 400; font-size: 24px; line-height: 1.15; }

  .info {
    position: absolute; left: 260px; width: 295px;
    text-align: right; color: var(--ink); font-size: 15px; line-height: 20px;
  }
  .info--intro { top: 330px; font-size: 13.5px; line-height: 18px; }
  .info--address { top: 515px; }
  .info--hours { top: 680px; }
  .info h2 { font-size: 16px; font-weight: 700; line-height: 22px; }
</style>
</head>
<body>
  <main class="flyer">
    <div class="photo photo--main" role="img" aria-label="Foto: veganes Hauptgericht mit Paprika, Bohnen und Sternanis"></div>
    <div class="photo photo--wrap" role="img" aria-label="Foto: gefüllter Wrap mit frischem Salat auf weißem Teller"></div>
    <div class="photo photo--dessert" role="img" aria-label="Foto: geschichtetes Dessert im Glas mit Beeren"></div>

    <div class="rule rule--top-v"></div>
    <div class="rule rule--band-t"></div>
    <div class="rule rule--band-b"></div>
    <div class="rule rule--col-v"></div>
    <div class="rule rule--row-1"></div>
    <div class="rule rule--row-2"></div>

    <header class="brand-band">
      <h1 class="brand-name">BASILIKUM</h1>
      <p class="brand-claim">Frisch, grün, pflanzlich!</p>
    </header>

    <p class="info info--intro">Das erste Restaurant mit rein<br>pflanzlichen Speisen und Getränken<br>in Frankfurt haben Sie gefunden …</p>

    <section class="info info--address">
      <h2>Adresse</h2>
      <p>Am Krautgarten 17<br>60385 Frankfurt am Main<br>Telefon: 069-24716380<br>Telefax: 069-24716381<br>hallo@basilikum-frankfurt.de<br>www.basilikum-frankfurt.de</p>
    </section>

    <section class="info info--hours">
      <h2>Öffnungszeiten</h2>
      <p>Dienstag – Freitag 18 – 23 Uhr<br>Samstag 18 – 24 Uhr<br>Sonntag 10 – 23 Uhr<br>Montag Ruhetag</p>
    </section>
  </main>
</body>
</html>
```